Group Medical Practice needs stationery, business cards etc. designed

We need stationery designed for a multisite practice that offers primary medical, dental and behavioral healthcare. We would like a design that is consistent for letterhead, business cards, Microsoft Outlook stationery etc. We have attached our new logo design.

```html
<!DOCTYPE html>
<html lang="en">
<head>
<meta charset="utf-8">
<title>Cedar Ridge Health Services – Stationery Set</title>
<link href="https://fonts.googleapis.com/css2?family=Libre+Baskerville:wght@400;700&family=Open+Sans:wght@400;600&display=swap" rel="stylesheet">
<style>
  :root{
    --brand-green:#7ff000;
    --brand-blue:#2a7cf0;
    --brand-name:#1f78d1;
    --band-grey:#7f8a8a;
    --paper:#ffffff;
    --paper-shade:#ececec;
    --ink:#222222;
    --rule:#555555;
    --stage:#efece7;
    --label:#4a4a4a;
  }
  *{box-sizing:border-box;margin:0;padding:0}
  html,body{width:1200px;height:540px;overflow:hidden;background:var(--stage)}
  .canvas{position:relative;width:1200px;height:540px;overflow:hidden;background:var(--stage);
    font-family:"Libre Baskerville",Georgia,serif;color:var(--ink)}
  .sheet{position:absolute;background:var(--paper);box-shadow:0 1px 4px rgba(0,0,0,.18);overflow:hidden}

  /* brand name lockup */
  .brand{position:absolute;display:flex;align-items:center;gap:4px}
  .brand-square{width:7px;height:7px;background:var(--brand-green);flex:none}
  .brand-name{font-family:"Libre Baskerville",Georgia,serif;font-weight:700;color:var(--brand-name);
    text-transform:uppercase;line-height:1.15;letter-spacing:.02em}
  .brand-name small{display:block;font-size:.62em;letter-spacing:.08em}

  .footer-band{position:absolute;left:0;bottom:0;width:100%}

  /* letterhead */
  .letterhead{left:20px;top:32px;width:343px;height:444px}
  .letterhead .brand{left:8px;top:30px}
  .letterhead .brand-name{font-size:8.5px}
  .contact-block{position:absolute;left:255px;top:10px;border-left:1px solid var(--ink);padding-left:5px;
    font-size:5.6px;line-height:9px}
  .contact-block li{list-style:none;display:flex;align-items:center;gap:4px}
  .contact-block svg{width:5px;height:5px;flex:none}
  .faint-name{position:absolute;left:0;width:100%;top:195px;text-align:center;font-weight:700;
    font-size:20px;color:var(--brand-green);opacity:.12;text-transform:uppercase;letter-spacing:.06em}
  .letterhead .address{position:absolute;bottom:14px;width:100%;text-align:center;font-size:7px;letter-spacing:.02em}

  /* fax */
  .fax{left:380px;top:32px;width:344px;height:444px;
    background:linear-gradient(180deg,#ffffff 0%,#f4f4f4 40%,var(--paper-shade) 100%)}
  .fax .brand{left:8px;top:30px}
  .fax .brand-name{font-size:8.5px}
  .fax .return-address{position:absolute;left:258px;top:18px;border-left:1px solid var(--ink);padding-left:4px;
    font-family:"Open Sans",Arial,sans-serif;font-size:6px;line-height:8px}
  .fax-title{position:absolute;left:10px;top:104px;font-family:"Open Sans",Arial,sans-serif;font-size:20px;font-weight:400}
  .fax-fields{position:absolute;left:10px;top:146px;width:318px;display:grid;grid-template-columns:176px 118px;column-gap:12px;row-gap:10px}
  .fax-field{font-family:"Open Sans",Arial,sans-serif;font-size:5px;border-bottom:.8px solid var(--rule);padding-bottom:2px;height:10px}
  .fax-options{position:absolute;left:10px;top:238px;display:flex;gap:13px;font-family:"Open Sans",Arial,sans-serif;font-size:5px}
  .fax-options span{display:flex;align-items:center;gap:4px}
  .fax-options i{display:inline-block;width:7px;height:7px;border:.8px solid var(--ink);background:#fff}
  .fax-footer{position:absolute;left:8px;bottom:8px;display:flex;gap:20px;font-size:5.6px}
  .fax-footer span{display:flex;align-items:center;gap:3px}
  .fax-footer svg{width:5px;height:5px}

  /* envelopes */
  .envelope{position:absolute;background:var(--paper);box-shadow:0 1px 4px rgba(0,0,0,.18);overflow:hidden}
  .envelope-back-green{left:798px;top:34px;width:383px;height:171px}
  .envelope-back-blue{left:786px;top:109px;width:383px;height:171px;background:linear-gradient(180deg,#fff,#e6e6e6)}
  .flap{position:absolute;left:0;top:0;width:100%}
  .envelope-back-blue .brand{left:0;width:100%;top:46px;justify-content:center}
  .envelope-back-blue .brand-name{color:#ffffff;font-size:7.5px;text-align:center}
  .envelope-front{left:749px;top:198px;width:384px;height:171px}
  .envelope-front .brand{left:5px;top:12px}
  .envelope-front .brand-name{font-size:8px}
  .envelope-front .address{position:absolute;left:5px;top:51px;font-size:7px;line-height:8.5px}
  .envelope-front .website{position:absolute;left:6px;bottom:13px;font-size:6.8px}

  /* business cards */
  .card{position:absolute;top:395px;width:141px;height:79px;background:var(--paper);box-shadow:0 1px 4px rgba(0,0,0,.18);overflow:hidden}
  .card .brand{left:0;width:100%;justify-content:center;top:16px}
  .card .brand-name{font-size:6.4px;text-align:center}
  .card-contact{left:738px}
  .card-contact .person{position:absolute;right:73px;top:47px;text-align:right;font-size:3.6px;line-height:4.6px}
  .card-contact .details{position:absolute;left:72px;top:47px;border-left:.6px solid var(--ink);padding-left:3px;font-size:3.4px;line-height:4.6px}
  .card-contact .details span{display:flex;align-items:center;gap:2px}
  .card-contact .details i{display:inline-block;width:3px;height:3px;border-radius:50%;background:var(--brand-blue)}
  .card-white{left:894px}
  .card-white .brand{top:26px}
  .card-blue{left:1039px;background:var(--brand-blue)}
  .card-blue .brand{top:26px}
  .card-blue .brand-name{color:#ffffff}
  .card .website{position:absolute;width:100%;text-align:center;top:58px;font-size:5.6px}
  .card-blue .website{color:#ffffff}

  .option-label{position:absolute;top:496px;font-family:"Open Sans",Arial,sans-serif;font-size:20px;color:var(--label)}
</style>
</head>
<body>
<main class="canvas">

  <!-- Letterhead -->
  <section class="sheet letterhead" aria-label="Letterhead">
    <div class="brand"><span class="brand-square"></span><span class="brand-name">Cedar Ridge<small>Health Services</small></span></div>
    <ul class="contact-block">
      <li><svg viewBox="0 0 10 10"><circle cx="5" cy="5" r="5" fill="#222"/></svg>123-456-7890</li>
      <li><svg viewBox="0 0 10 10"><circle cx="5" cy="5" r="5" fill="#222"/></svg>123-456-7856</li>
      <li><svg viewBox="0 0 10 10"><rect x="0" y="2" width="10" height="6" fill="#222"/></svg>cedarridgehs@mail.com</li>
      <li><svg viewBox="0 0 10 10"><circle cx="5" cy="5" r="5" fill="#222"/></svg>www.cedarridgehs.com</li>
    </ul>
    <p class="faint-name">Cedar Ridge</p>
    <p class="address">Street Name, City Name State Zipcode</p>
    <svg class="footer-band" viewBox="0 0 343 9" height="9" preserveAspectRatio="none">
      <polygon points="0,0 168,0 160,9 0,9" fill="var(--band-grey)"/>
      <polygon points="172,3 343,3 343,9 164,9" fill="var(--brand-blue)"/>
    </svg>
  </section>

  <!-- Fax sheet -->
  <section class="sheet fax" aria-label="Fax cover sheet">
    <div class="brand"><span class="brand-square"></span><span class="brand-name">Cedar Ridge<small>Health Services</small></span></div>
    <p class="return-address">Street Name, City Name<br>State Zipcode</p>
    <h1 class="fax-title">FAX</h1>
    <div class="fax-fields">
      <div class="fax-field">To :</div><div class="fax-field">From :</div>
      <div class="fax-field">Fax :</div><div class="fax-field">Pages :</div>
      <div class="fax-field">Phone :</div><div class="fax-field">Date :</div>
      <div class="fax-field">Re :</div><div class="fax-field">CC :</div>
    </div>
    <div class="fax-options">
      <span><i></i>Urgent</span><span><i></i>For Review</span><span><i></i>Please Comment</span>
      <span><i></i>Please Reply</span><span><i></i>Please Recycle</span>
    </div>
    <div class="fax-footer">
      <span><svg viewBox="0 0 10 10"><circle cx="5" cy="5" r="5" fill="var(--brand-blue)"/></svg>123-456-7890</span>
      <span><svg viewBox="0 0 10 10"><circle cx="5" cy="5" r="5" fill="var(--brand-blue)"/></svg>123-456-7856</span>
      <span><svg viewBox="0 0 10 10"><rect y="2" width="10" height="6" fill="var(--brand-blue)"/></svg>cedarridgehs@mail.com</span>
      <span><svg viewBox="0 0 10 10"><circle cx="5" cy="5" r="5" fill="var(--brand-blue)"/></svg>www.cedarridgehs.com</span>
    </div>
  </section>

  <!-- Envelope backs -->
  <section class="envelope envelope-back-green" aria-label="Envelope back, green flap">
    <svg class="flap" viewBox="0 0 383 110" height="110" preserveAspectRatio="none">
      <path d="M0,0 H383 V12 Q300,60 205,100 Q191,106 177,100 Q83,60 0,12 Z" fill="var(--brand-green)"/>
    </svg>
  </section>
  <section class="envelope envelope-back-blue" aria-label="Envelope back, blue flap">
    <svg class="flap" viewBox="0 0 383 110" height="110" preserveAspectRatio="none">
      <path d="M0,0 H383 V12 Q300,60 205,100 Q191,106 177,100 Q83,60 0,12 Z" fill="var(--brand-blue)"/>
    </svg>
    <div class="brand"><span class="brand-name">Cedar Ridge<small>Health Services</small></span></div>
  </section>

  <!-- Envelope front -->
  <section class="envelope envelope-front" aria-label="Envelope front">
    <div class="brand"><span class="brand-square"></span><span class="brand-name">Cedar Ridge<small>Health Services</small></span></div>
    <p class="address">Street Name, City Name<br>State Zipcode</p>
    <p class="website">www.cedarridgehs.com</p>
    <svg class="footer-band" viewBox="0 0 384 9" height="9" preserveAspectRatio="none">
      <polygon points="0,0 188,0 180,9 0,9" fill="var(--band-grey)"/>
      <polygon points="192,3 384,0 384,9 184,9" fill="var(--brand-blue)"/>
    </svg>
  </section>

  <!-- Business cards -->
  <section class="card card-contact" aria-label="Business card front">
    <div class="brand"><span class="brand-square"></span><span class="brand-name">Cedar Ridge<small>Health Services</small></span></div>
    <p class="person">Your Name<br>Title<br><br>Street Name City Name<br>State Zip Code</p>
    <div class="details">
      <span><i></i>123-456-7890</span>
      <span><i></i>123-456-7856</span>
      <span><i></i>cedarridgehs@mail.com</span>
      <span><i></i>www.cedarridgehs.com</span>
    </div>
    <svg class="footer-band" viewBox="0 0 141 4" height="4" preserveAspectRatio="none">
      <polygon points="0,0 70,0 66,4 0,4" fill="var(--band-grey)"/>
      <polygon points="72,1 141,1 141,4 68,4" fill="var(--brand-blue)"/>
    </svg>
  </section>
  <section class="card card-white" aria-label="Business card back, white">
    <div class="brand"><span class="brand-square"></span><span class="brand-name">Cedar Ridge<small>Health Services</small></span></div>
    <p class="website">www.cedarridgehs.com</p>
  </section>
  <section class="card card-blue" aria-label="Business card back, blue">
    <div class="brand"><span class="brand-square"></span><span class="brand-name">Cedar Ridge<small>Health Services</small></span></div>
    <p class="website">www.cedarridgehs.com</p>
  </section>

  <p class="option-label" style="left:117px">Option-1</p>
  <p class="option-label" style="left:506px">Option-2</p>
</main>
</body>
</html>
```